New Modern floristry business design

Hi, we are a new business based in Sydney called "velvet moss floristry"

With so many floristry's we need a good design that will set a great first impression.

A few descriptive words on how we envision velvet moss floristry:

-dynamic design
-minimal colour (colour can be used to enhance the design)
-black white grey (can include gold,silver,metallic shadowing)
Strong "VELVET MOSS" with a classy "FLORISTRY"
Bold with a touch of feminine

Industry/Entity Type

Business

Contact Information for Business Card

Velvet Moss Floristry,
Delphine Ruvek,
Velvetmossfloristry@quillmail.com.au

```html
<!DOCTYPE html>
<html lang="en">
<head>
<meta charset="utf-8">
<title>Velvet Moss Floristry – Business Cards</title>
<link href="https://fonts.googleapis.com/css2?family=Didact+Gothic&family=Kaushan+Script&display=swap" rel="stylesheet">
<style>
  :root {
    --backdrop: #2f2c2e;
    --card-light: #ffffff;
    --card-dark: #4c5051;
    --ink-dark: #4a4a4a;
    --ink-light: #ffffff;
    --mark-green: #5aa83a;
  }
  html, body {
    margin: 0;
    padding: 0;
    width: 1200px;
    height: 800px;
    overflow: hidden;
    background: var(--backdrop);
  }
  .canvas {
    position: relative;
    width: 1200px;
    height: 800px;
  }
  .card {
    position: absolute;
    width: 476px;
    height: 278px;
    border-radius: 12px;
    display: flex;
    flex-direction: column;
    align-items: center;
    box-sizing: border-box;
  }
  .card--light { background: var(--card-light); color: var(--ink-dark); }
  .card--dark  { background: var(--card-dark);  color: var(--ink-light); }
  .card--row1 { top: 75px; }
  .card--row2 { top: 447px; }
  .card--left  { left: 90px; }
  .card--right { left: 634px; }

  /* contact side */
  .contact { padding-top: 95px; }
  .mail-icon { width: 52px; height: 52px; display: block; }
  .mail-icon .badge { fill: currentColor; }
  .card--light .mail-icon .glyph { stroke: var(--card-light); }
  .card--dark  .mail-icon .glyph { stroke: var(--card-dark); }
  .email {
    margin-top: 6px;
    font-family: "Didact Gothic", "Helvetica Neue", Arial, sans-serif;
    font-size: 20px;
    letter-spacing: 0.2px;
  }

  /* brand side */
  .brand { padding-top: 98px; }
  .wordmark {
    display: flex;
    align-items: center;
    gap: 12px;
  }
  .wordmark__dot {
    width: 30px;
    height: 30px;
    border-radius: 50%;
    background: var(--mark-green);
    flex: none;
  }
  .wordmark__name {
    font-family: "Didact Gothic", "Helvetica Neue", Arial, sans-serif;
    font-size: 30px;
    line-height: 1;
  }
  .person {
    margin-top: 50px;
    font-family: "Kaushan Script", "Brush Script MT", cursive;
    font-size: 21px;
  }
</style>
</head>
<body>
<main class="canvas">

  <section class="card card--light card--row1 card--left contact">
    <svg class="mail-icon" viewBox="0 0 52 52" aria-hidden="true">
      <circle class="badge" cx="26" cy="26" r="25"/>
      <g class="glyph" fill="none" stroke-width="2.4" stroke-linejoin="round">
        <rect x="13" y="17" width="26" height="18" rx="1.5"/>
        <path d="M13 18 L26 28 L39 18"/>
      </g>
    </svg>
    <p class="email">Velvetmossfloristry@quillmail.com.au</p>
  </section>

  <section class="card card--light card--row1 card--right brand">
    <div class="wordmark">
      <span class="wordmark__dot"></span>
      <span class="wordmark__name">Velvet Moss Floristry</span>
    </div>
    <p class="person">Delphine Ruvek</p>
  </section>

  <section class="card card--dark card--row2 card--left contact">
    <svg class="mail-icon" viewBox="0 0 52 52" aria-hidden="true">
      <circle class="badge" cx="26" cy="26" r="25"/>
      <g class="glyph" fill="none" stroke-width="2.4" stroke-linejoin="round">
        <rect x="13" y="17" width="26" height="18" rx="1.5"/>
        <path d="M13 18 L26 28 L39 18"/>
      </g>
    </svg>
    <p class="email">Velvetmossfloristry@quillmail.com.au</p>
  </section>

  <section class="card card--dark card--row2 card--right brand">
    <div class="wordmark">
      <span class="wordmark__dot"></span>
      <span class="wordmark__name">Velvet Moss Floristry</span>
    </div>
    <p class="person">Delphine Ruvek</p>
  </section>

</main>
</body>
</html>
```